Custom Mexican Train Dominos Scorecard

My wife and I regularly play Mexican Train dominos with our friends and family and would like to create a series of custom scorecards specific to our various groups that we play with. The idea would be to have them printed on pads or in notebooks that over time will hold a record of all of our games. Searching around on the web, the only "off the shelf" that I see are pretty plain and boring (see attached). We would love something with a fun and playful mid-century graphic feel to it. Can be a single color or more than one. We want to have the player names incorporated into the design, so for the first one the names would be Tessa, Harold, Ruth & Colin. We will want a place to date each card and of course boxes to fill out the score. I have included a few examples of how the scorecard is basically laid out. Can be any size and can be done in landscape or portrait. I think I would just like the title to say "Domino Night" or potentially no title at all with just a fun domino graphic. Thank you!

Requirements
Must have
• Basic score layout
Nice to have
• nothing in particular
Should not have
• nothing in particular

```html
<!DOCTYPE html>
<html lang="en">
<head>
<meta charset="utf-8">
<title>Domino Night – Mexican Train Scorecard</title>
<link href="https://fonts.googleapis.com/css2?family=Permanent+Marker&family=Open+Sans:wght@700&display=block" rel="stylesheet">
<style>
  :root {
    --ink: #1e1e1e;
    --paper: #ffffff;
    --bg-centre: #ffffff;
    --bg-edge: #e8e7e7;
    --rule: #2a2a2a;
    --art-light: #b8b8b8;
    --art-dark: #6f6f6f;
  }
  html, body { margin: 0; padding: 0; overflow: hidden; }
  body {
    width: 1200px; height: 1200px;
    background: radial-gradient(circle at 50% 50%, var(--bg-centre) 0%, var(--bg-centre) 25%, var(--bg-edge) 100%);
    position: relative;
    color: var(--ink);
  }
  .brush {
    font-family: 'Permanent Marker', 'Marker Felt', 'Comic Sans MS', cursive;
    font-weight: 400;
    font-style: normal;
  }
  .scorecard {
    position: absolute; left: 390px; top: 302px;
    width: 420px; height: 595px;
    box-sizing: border-box;
    border: 1px solid #555;
    background: var(--paper);
  }
  .title {
    position: absolute; left: 0; right: 0; top: 16px;
    margin: 0; text-align: center;
    font-size: 44px; line-height: 1;
    white-space: nowrap;
  }
  .subtitle {
    position: absolute; left: 143px; width: 134px; top: 71px;
    margin: 0; text-align: center;
    font-size: 15px; line-height: 1;
    white-space: nowrap;
  }
  .train-art {
    position: absolute; top: 70px; width: 42px; height: 30px;
    background: linear-gradient(180deg, var(--art-light), var(--art-dark));
    border-radius: 3px;
  }
  .train-art.left { left: 99px; }
  .train-art.right { left: 279px; }
  .date-line {
    position: absolute; right: 20px; top: 102px;
    font-size: 9px; line-height: 1; white-space: nowrap;
  }
  .score-table {
    position: absolute; left: 26px; top: 117px;
    width: 373px; border-collapse: collapse; table-layout: fixed;
  }
  .score-table td, .score-table th {
    border: 1px solid var(--rule); padding: 0;
  }
  .score-table col.label { width: 98px; }
  .head-row { height: 39px; }
  .head-row th { font-size: 12px; text-transform: uppercase; }
  .head-row th.players { font-size: 16px; text-transform: none; }
  .round-row { height: 28.4px; }
  .round-label { display: flex; align-items: center; padding-left: 7px; gap: 8px; height: 27px; }
  .domino { width: 51px; height: 22px; display: block; }
  .round-num {
    font-family: 'Open Sans', Arial, sans-serif; font-weight: 700;
    font-size: 18px; width: 26px; text-align: center;
  }
  .subtotal-label, .total-label { font-size: 14px; text-align: center; }
  .spacer-row { height: 9px; }
  .total-row { height: 28px; }
</style>
</head>
<body>
<svg width="0" height="0" style="position:absolute">
  <defs>
    <symbol id="pips-12" viewBox="0 0 24 22"><g fill="#1e1e1e"><circle cx="5" cy="4" r="1.6"/><circle cx="12" cy="4" r="1.6"/><circle cx="19" cy="4" r="1.6"/><circle cx="5" cy="9" r="1.6"/><circle cx="12" cy="9" r="1.6"/><circle cx="19" cy="9" r="1.6"/><circle cx="5" cy="13" r="1.6"/><circle cx="12" cy="13" r="1.6"/><circle cx="19" cy="13" r="1.6"/><circle cx="5" cy="18" r="1.6"/><circle cx="12" cy="18" r="1.6"/><circle cx="19" cy="18" r="1.6"/></g></symbol>
    <symbol id="pips-11" viewBox="0 0 24 22"><g fill="#1e1e1e"><circle cx="5" cy="4" r="1.6"/><circle cx="19" cy="4" r="1.6"/><circle cx="5" cy="9" r="1.6"/><circle cx="19" cy="9" r="1.6"/><circle cx="5" cy="13" r="1.6"/><circle cx="19" cy="13" r="1.6"/><circle cx="5" cy="18" r="1.6"/><circle cx="19" cy="18" r="1.6"/><circle cx="12" cy="4" r="1.6"/><circle cx="12" cy="11" r="1.6"/><circle cx="12" cy="18" r="1.6"/></g></symbol>
    <symbol id="pips-10" viewBox="0 0 24 22"><g fill="#1e1e1e"><circle cx="5" cy="4" r="1.6"/><circle cx="19" cy="4" r="1.6"/><circle cx="5" cy="9" r="1.6"/><circle cx="19" cy="9" r="1.6"/><circle cx="5" cy="13" r="1.6"/><circle cx="19" cy="13" r="1.6"/><circle cx="5" cy="18" r="1.6"/><circle cx="19" cy="18" r="1.6"/><circle cx="12" cy="9" r="1.6"/><circle cx="12" cy="13" r="1.6"/></g></symbol>
    <symbol id="pips-9" viewBox="0 0 24 22"><g fill="#1e1e1e"><circle cx="5" cy="4" r="1.6"/><circle cx="12" cy="4" r="1.6"/><circle cx="19" cy="4" r="1.6"/><circle cx="5" cy="11" r="1.6"/><circle cx="12" cy="11" r="1.6"/><circle cx="19" cy="11" r="1.6"/><circle cx="5" cy="18" r="1.6"/><circle cx="12" cy="18" r="1.6"/><circle cx="19" cy="18" r="1.6"/></g></symbol>
    <symbol id="pips-8" viewBox="0 0 24 22"><g fill="#1e1e1e"><circle cx="5" cy="4" r="1.6"/><circle cx="12" cy="4" r="1.6"/><circle cx="19" cy="4" r="1.6"/><circle cx="5" cy="11" r="1.6"/><circle cx="19" cy="11" r="1.6"/><circle cx="5" cy="18" r="1.6"/><circle cx="12" cy="18" r="1.6"/><circle cx="19" cy="18" r="1.6"/></g></symbol>
    <symbol id="pips-7" viewBox="0 0 24 22"><g fill="#1e1e1e"><circle cx="5" cy="4" r="1.6"/><circle cx="19" cy="4" r="1.6"/><circle cx="5" cy="11" r="1.6"/><circle cx="12" cy="11" r="1.6"/><circle cx="19" cy="11" r="1.6"/><circle cx="5" cy="18" r="1.6"/><circle cx="19" cy="18" r="1.6"/></g></symbol>
    <symbol id="pips-6" viewBox="0 0 24 22"><g fill="#1e1e1e"><circle cx="5" cy="4" r="1.6"/><circle cx="19" cy="4" r="1.6"/><circle cx="5" cy="11" r="1.6"/><circle cx="19" cy="11" r="1.6"/><circle cx="5" cy="18" r="1.6"/><circle cx="19" cy="18" r="1.6"/></g></symbol>
    <symbol id="pips-5" viewBox="0 0 24 22"><g fill="#1e1e1e"><circle cx="5" cy="4" r="1.6"/><circle cx="19" cy="4" r="1.6"/><circle cx="12" cy="11" r="1.6"/><circle cx="5" cy="18" r="1.6"/><circle cx="19" cy="18" r="1.6"/></g></symbol>
    <symbol id="pips-4" viewBox="0 0 24 22"><g fill="#1e1e1e"><circle cx="5" cy="4" r="1.6"/><circle cx="19" cy="4" r="1.6"/><circle cx="5" cy="18" r="1.6"/><circle cx="19" cy="18" r="1.6"/></g></symbol>
    <symbol id="pips-3" viewBox="0 0 24 22"><g fill="#1e1e1e"><circle cx="5" cy="4" r="1.6"/><circle cx="12" cy="11" r="1.6"/><circle cx="19" cy="18" r="1.6"/></g></symbol>
    <symbol id="pips-2" viewBox="0 0 24 22"><g fill="#1e1e1e"><circle cx="5" cy="4" r="1.6"/><circle cx="19" cy="18" r="1.6"/></g></symbol>
    <symbol id="pips-1" viewBox="0 0 24 22"><g fill="#1e1e1e"><circle cx="12" cy="11" r="1.6"/></g></symbol>
    <symbol id="tile" viewBox="0 0 51 22"><rect x="0.5" y="0.5" width="50" height="21" rx="1.5" fill="#fff" stroke="#1e1e1e" stroke-width="0.8"/><line x1="25.5" y1="0.5" x2="25.5" y2="21.5" stroke="#1e1e1e" stroke-width="0.8"/></symbol>
  </defs>
</svg>

<main class="scorecard">
  <h1 class="title brush">DOMINO NIGHT</h1>
  <div class="train-art left" role="img" aria-label="Steam locomotive illustration"></div>
  <p class="subtitle brush">MEXICAN TRAIN</p>
  <div class="train-art right" role="img" aria-label="Steam locomotive illustration"></div>
  <div class="date-line brush">DATE : ..... / ..... / ......</div>

  <table class="score-table">
    <colgroup><col class="label"><col><col><col><col></colgroup>
    <tr class="head-row brush">
      <th class="players brush">Players</th><th class="brush">Tessa</th><th class="brush">Harold</th><th class="brush">Ruth</th><th class="brush">Colin</th>
    </tr>
    <tr class="round-row"><td><div class="round-label"><svg class="domino" viewBox="0 0 51 22"><use href="#tile"/><use href="#pips-12" x="1" width="24" height="22"/><use href="#pips-12" x="26" width="24" height="22"/></svg><span class="round-num">12</span></div></td><td></td><td></td><td></td><td></td></tr>
    <tr class="round-row"><td><div class="round-label"><svg class="domino" viewBox="0 0 51 22"><use href="#tile"/><use href="#pips-11" x="1" width="24" height="22"/><use href="#pips-11" x="26" width="24" height="22"/></svg><span class="round-num">11</span></div></td><td></td><td></td><td></td><td></td></tr>
    <tr class="round-row"><td><div class="round-label"><svg class="domino" viewBox="0 0 51 22"><use href="#tile"/><use href="#pips-10" x="1" width="24" height="22"/><use href="#pips-10" x="26" width="24" height="22"/></svg><span class="round-num">10</span></div></td><td></td><td></td><td></td><td></td></tr>
    <tr class="round-row"><td><div class="round-label"><svg class="domino" viewBox="0 0 51 22"><use href="#tile"/><use href="#pips-9" x="1" width="24" height="22"/><use href="#pips-9" x="26" width="24" height="22"/></svg><span class="round-num">9</span></div></td><td></td><td></td><td></td><td></td></tr>
    <tr class="round-row"><td><div class="round-label"><svg class="domino" viewBox="0 0 51 22"><use href="#tile"/><use href="#pips-8" x="1" width="24" height="22"/><use href="#pips-8" x="26" width="24" height="22"/></svg><span class="round-num">8</span></div></td><td></td><td></td><td></td><td></td></tr>
    <tr class="round-row"><td><div class="round-label"><svg class="domino" viewBox="0 0 51 22"><use href="#tile"/><use href="#pips-7" x="1" width="24" height="22"/><use href="#pips-7" x="26" width="24" height="22"/></svg><span class="round-num">7</span></div></td><td></td><td></td><td></td><td></td></tr>
    <tr class="round-row"><td class="subtotal-label brush">Sub Total</td><td></td><td></td><td></td><td></td></tr>
    <tr class="round-row"><td><div class="round-label"><svg class="domino" viewBox="0 0 51 22"><use href="#tile"/><use href="#pips-6" x="1" width="24" height="22"/><use href="#pips-6" x="26" width="24" height="22"/></svg><span class="round-num">6</span></div></td><td></td><td></td><td></td><td></td></tr>
    <tr class="round-row"><td><div class="round-label"><svg class="domino" viewBox="0 0 51 22"><use href="#tile"/><use href="#pips-5" x="1" width="24" height="22"/><use href="#pips-5" x="26" width="24" height="22"/></svg><span class="round-num">5</span></div></td><td></td><td></td><td></td><td></td></tr>
    <tr class="round-row"><td><div class="round-label"><svg class="domino" viewBox="0 0 51 22"><use href="#tile"/><use href="#pips-4" x="1" width="24" height="22"/><use href="#pips-4" x="26" width="24" height="22"/></svg><span class="round-num">4</span></div></td><td></td><td></td><td></td><td></td></tr>
    <tr class="round-row"><td><div class="round-label"><svg class="domino" viewBox="0 0 51 22"><use href="#tile"/><use href="#pips-3" x="1" width="24" height="22"/><use href="#pips-3" x="26" width="24" height="22"/></svg><span class="round-num">3</span></div></td><td></td><td></td><td></td><td></td></tr>
    <tr class="round-row"><td><div class="round-label"><svg class="domino" viewBox="0 0 51 22"><use href="#tile"/><use href="#pips-2" x="1" width="24" height="22"/><use href="#pips-2" x="26" width="24" height="22"/></svg><span class="round-num">2</span></div></td><td></td><td></td><td></td><td></td></tr>
    <tr class="round-row"><td><div class="round-label"><svg class="domino" viewBox="0 0 51 22"><use href="#tile"/><use href="#pips-1" x="1" width="24" height="22"/><use href="#pips-1" x="26" width="24" height="22"/></svg><span class="round-num">1</span></div></td><td></td><td></td><td></td><td></td></tr>
    <tr class="round-row"><td><div class="round-label"><svg class="domino" viewBox="0 0 51 22"><use href="#tile"/><use href="#pips-1" x="1" width="24" height="22"/><use href="#pips-1" x="26" width="24" height="22"/></svg><span class="round-num">0</span></div></td><td></td><td></td><td></td><td></td></tr>
    <tr class="spacer-row"><td></td><td></td><td></td><td></td><td></td></tr>
    <tr class="total-row"><td class="total-label brush">Game Total</td><td></td><td></td><td></td><td></td></tr>
  </table>
</main>
</body>
</html>
```